Torvelin Business Card

We need a business card design. We have a logo from a previous PixelHarbor project and I am attaching the logo files in jpeg and photoshop.

Business

```html
<!DOCTYPE html>
<html lang="en">
<head>
<meta charset="utf-8">
<title>Torvelin Business Card</title>
<link rel="stylesheet" href="https://fonts.googleapis.com/css2?family=Arimo:wght@400;700&family=Roboto+Condensed:wght@400&display=swap">
<style>
  :root {
    --paper: #fcfcfa;
    --ink: #111111;
    --brand-dark: #454545;
    --brand-green: #5ab52f;
    --band: #c0c0c0;
    --band-edge: #dcdcdc;
  }
  * { margin: 0; padding: 0; box-sizing: border-box; }
  html, body {
    width: 1200px; height: 720px; overflow: hidden;
    background: var(--paper);
  }
  .card {
    position: relative; width: 1200px; height: 720px;
    background: var(--paper);
    font-family: "Arimo", Arial, sans-serif;
    color: var(--ink);
  }
  .holder-name {
    position: absolute; left: 76px; top: 80px;
    font-size: 47px; font-weight: 400; line-height: 1;
  }
  .holder-role {
    position: absolute; left: 152px; top: 146px;
    font-size: 29px; color: var(--brand-green); line-height: 1;
  }
  .contact-row {
    position: absolute; display: flex; align-items: center;
    font-size: 29px; line-height: 1; letter-spacing: 0.5px;
  }
  .contact-row svg { position: absolute; fill: var(--brand-green); }
  .phone { left: 877px; top: 90px; }
  .fax { left: 877px; top: 133px; }
  .phone svg { left: -58px; width: 20px; height: 30px; }
  .fax svg { left: -63px; width: 32px; height: 30px; }
  .web { left: 154px; top: 518px; }
  .mail { left: 154px; top: 563px; }
  .web svg { left: -66px; width: 34px; height: 34px; }
  .mail svg { left: -64px; width: 30px; height: 22px; }

  .brand {
    position: absolute; left: 0; right: 0; top: 258px;
    display: flex; justify-content: center; align-items: center; gap: 26px;
  }
  .brand-mark {
    width: 62px; height: 62px; background: var(--brand-green);
  }
  .brand-name {
    font-family: "Arimo", Arial, sans-serif;
    font-weight: 700; font-size: 92px; line-height: 1;
    color: var(--brand-dark); letter-spacing: -2px;
  }

  .address-pin {
    position: absolute; left: 811px; top: 504px;
    width: 26px; height: 36px; fill: var(--brand-green);
  }
  .address {
    position: absolute; left: 880px; top: 514px;
    font-family: "Roboto Condensed", "Arial Narrow", sans-serif;
    font-size: 29px; line-height: 27px; text-transform: uppercase;
    letter-spacing: -0.5px;
  }
  .band-edge {
    position: absolute; left: 0; top: 627px; width: 1200px; height: 13px;
    background: var(--band-edge);
  }
  .band {
    position: absolute; left: 0; top: 640px; width: 1200px; height: 80px;
    background: var(--band);
  }
</style>
</head>
<body>
<main class="card">
  <h1 class="holder-name">Ravin K</h1>
  <p class="holder-role">Designer</p>

  <p class="contact-row phone">
    <svg viewBox="0 0 20 30" aria-hidden="true"><path d="M4 1h6v7H7c-1 4-1 10 0 14h3v7H4C0 21 0 9 4 1z"/></svg>
    +91 123456789
  </p>
  <p class="contact-row fax">
    <svg viewBox="0 0 32 30" aria-hidden="true"><path d="M9 1h14v10H9z M1 13h30v16H1z" /><rect x="5" y="17" width="22" height="3" fill="#fcfcfa"/><rect x="5" y="23" width="22" height="3" fill="#fcfcfa"/></svg>
    +91 123456789
  </p>

  <div class="brand">
    <span class="brand-mark" aria-hidden="true"></span>
    <span class="brand-name">Torvelin</span>
  </div>

  <p class="contact-row web">
    <svg viewBox="0 0 34 34" aria-hidden="true"><circle cx="17" cy="17" r="16"/><path d="M6 12c4-1 6 2 9 1s3 5 0 7-3 6-5 8c-3-2-6-7-4-16zM21 5c3 1 4 4 3 6s2 4 5 4c0 5-3 9-6 11 0-4-3-6-1-9s-3-5-1-12z" fill="#fcfcfa"/></svg>
    www.yourwebsite.com
  </p>
  <p class="contact-row mail">
    <svg viewBox="0 0 30 22" aria-hidden="true"><path d="M0 0h30v22H0z M3 3v16h24V3z M3 3l12 10L27 3v3L15 16 3 6z"/></svg>
    ravin@email.com
  </p>

  <svg class="address-pin" viewBox="0 0 26 36" aria-hidden="true"><path d="M13 0C5 0 0 6 0 13c0 8 13 23 13 23s13-15 13-23C26 6 21 0 13 0z"/><circle cx="13" cy="13" r="4.5" fill="#fcfcfa"/></svg>
  <address class="address" style="font-style:normal">
    Business Name<br>
    1234 Street Name<br>
    City, State 12345
  </address>

  <div class="band-edge" aria-hidden="true"></div>
  <div class="band" aria-hidden="true"></div>
</main>
</body>
</html>
```